Consultative Employee Benifits Firm Needs Business Card Design Project

We need a business card design for a new company based in Northern Virginia called "Telman Financial Services, LLC. We are both a wealth management advisory firm, as well as an employee benefits firm, which strives to provide superior creativity in employee benefits plan design and greater client and employee satisfaction. We are obsessed with service and follow up.

Our firm specializes in the areas of group health, life, dental, disability, voluntary benefits, Executive Benefits, HRA and HSA programs. We offer competitive employee benefit packages and pricing models for single or multi-state/multi location companies by maintaining preferred relationships with a large number of regional and national carriers.

Our firm also considers the many dimensions of your wealth through an integrated process we call wealth structuring — a comprehensive, dynamic approach to building, preserving, enjoying and transferring your wealth. And because we are often dealing with complex ownership structures and complicated, changing family dynamics, we bring the highest level of experience and creativity to managing your wealth. We work hard to help ensure that your legacy lasts by preparing your children for the financial challenges and opportunities that are headed their way.

Our final design should communicate an integrated approach to finanial safety and optimization
Updates

 Due to a few designers not accepting due to low budget, I have increased budget payout 19%. 

Project Deadline Extended
Reason: I have only heard from 12 designers. So, maybe I did not give the right amount of time to do the project. For the designers that have submitted their designs, thank you. I have seen three or four designs that I liked and might end up with one of them after it's all over, but I thought I would see between 20 - 25 before everything was over. Dan

Target Market(s)

Professionals; doctors, contractors, small to mid size business owners, ages 50 -65 with nert worth of 2MM

Industry/Entity Type

Financial

Requirements
Must have
• Telman Financial Services, LLC

Dan Telman
President
41957 Marwick Hollow Street
Quenford Glen, 20871

Office: 703 555-0184
Cell: 703 555-0127
Fax: 703 555-0163
Email: dantelman@quorvex.net
Should not have
• No pink or yellow colors.
No generic clipart (coins, dollar signs, money bags, graphs)

```html
<!DOCTYPE html>
<html lang="en">
<head>
<meta charset="utf-8">
<title>Telman Financial Services, LLC – Business Card</title>
<link rel="stylesheet" href="https://fonts.googleapis.com/css2?family=Questrial&family=Marcellus&display=swap">
<style>
  :root {
    --card-bg: #262728;
    --firm-blue: #2c54a4;
    --firm-blue-dark: #1b3570;
    --wave-dark: #213671;
    --wave-light: #3e67ae;
    --wave-edge: #1c2c5e;
    --text-light: #f4f4f4;
  }
  html, body {
    margin: 0;
    padding: 0;
    width: 1200px;
    height: 700px;
    overflow: hidden;
    background: var(--card-bg);
  }
  .card {
    position: relative;
    width: 1200px;
    height: 700px;
    background: var(--card-bg);
    overflow: hidden;
    font-family: "Questrial", sans-serif;
    color: var(--text-light);
  }
  .card__wave {
    position: absolute;
    inset: 0;
    width: 1200px;
    height: 700px;
  }
  .firm-name {
    position: absolute;
    left: 46px;
    top: 38px;
    margin: 0;
    font-family: "Questrial", sans-serif;
    font-weight: 400;
    font-size: 82px;
    line-height: 84px;
    letter-spacing: -1px;
    color: var(--firm-blue);
    text-shadow: 0 2px 3px rgba(0, 0, 0, 0.6);
  }
  .person {
    position: absolute;
    right: 64px;
    top: 220px;
    text-align: right;
  }
  .person__name {
    margin: 0;
    font-family: "Marcellus", serif;
    font-weight: 400;
    font-size: 72px;
    line-height: 80px;
    color: #ffffff;
  }
  .person__title {
    margin: 0;
    font-size: 38px;
    line-height: 42px;
    letter-spacing: 0.5px;
  }
  .address {
    position: absolute;
    left: 56px;
    top: 386px;
    margin: 0;
    font-style: normal;
    font-size: 38px;
    line-height: 51px;
  }
  .contact {
    position: absolute;
    top: 565px;
    margin: 0;
    font-size: 33px;
    line-height: 46px;
  }
  .contact--phones { left: 56px; }
  .contact--remote { left: 668px; }
</style>
</head>
<body>
  <div class="card">
    <svg class="card__wave" viewBox="0 0 1200 700" aria-hidden="true">
      <defs>
        <linearGradient id="waveFill" x1="0" y1="0" x2="1" y2="0">
          <stop offset="0" stop-color="var(--wave-dark)"/>
          <stop offset="1" stop-color="var(--wave-light)"/>
        </linearGradient>
      </defs>
      <path fill="var(--wave-edge)" d="M0,545 C300,538 560,470 780,405 C960,352 1080,340 1200,336 L1200,700 L0,700 Z"/>
      <path fill="url(#waveFill)" d="M0,558 C300,550 570,482 790,418 C970,366 1090,352 1200,348 L1200,700 L0,700 Z"/>
    </svg>

    <h1 class="firm-name">Telman Financial<br>Services,&nbsp; LLC</h1>

    <div class="person">
      <p class="person__name">Dan Telman</p>
      <p class="person__title">President</p>
    </div>

    <address class="address">
      41957 Marwick Hollow Street<br>
      Quenford Glen, 20871
    </address>

    <p class="contact contact--phones">
      Office: 703 555-0184<br>
      Cell: 703 555-0127
    </p>
    <p class="contact contact--remote">
      Fax: 703 555-0163<br>
      Email: dantelman@quorvex.net
    </p>
  </div>
</body>
</html>
```